Wren Pasco Copywriter Website

I am starting a new business as a freelance copywriter. Trying to set up the website for my business is proving to be too technical for me. I would like a simple, clean website using primarily black and white. I have attached the logo I would like used. I would like the menu icons to be Home, Services, Portfolio, Blog, Contact. I would like my mobile phone number (0438 526 914) and email address (wren.pasco.copywriter@mailbrook.example) used in the header of the site. I need the site to be easily manageable and inter-changeable for me to be able to move things around and add images, etc with ease.

I would like the home page to be a static page with space for an image of myself somewhere (I haven't had this taken as yet), an area to put a bit about myself and my business, and also somewhere to include social media icons/links. Again, I would like the whole website and home page to be easily managed so that I can add/delete things with ease.

I would like the image of the typewriter used in the website somewhere also please.

Coding

Number of Pages Required

Font styles to use
Sans Serif
Script

Colors
fdf0f6

Requirements
Must have
• The logo provided
• Ability to change page contents easily
• Ability to add social media icons as needed
Nice to have
• Use of the typewriter image
Should not have
• Complicated pages that are not easily editable

```html
<!DOCTYPE html>
<html lang="en">
<head>
<meta charset="utf-8">
<title>Wren Pasco — Copywriter</title>
<link rel="stylesheet" href="https://fonts.googleapis.com/css2?family=Great+Vibes&family=Mulish:wght@400;600;700&family=Open+Sans:wght@400;600;700&display=swap">
<style>
:root{
  --ink:#1c1c1c;
  --text:#444444;
  --muted:#6b6b6b;
  --blush:#f5e5e6;
  --rose:#d3868a;
  --line:#d8d8d8;
  --white:#ffffff;
  --script:"Great Vibes", cursive;
  --sans:"Mulish", sans-serif;
  --body:"Open Sans", sans-serif;
}
*{box-sizing:border-box;margin:0;padding:0}
html,body{width:1200px;height:2258px;overflow:hidden;background:var(--white)}
body{position:relative;font-family:var(--sans);color:var(--ink)}
.abs{position:absolute}

/* header */
.brand{left:96px;top:34px;font-family:var(--sans);font-weight:600;font-size:34px;color:var(--ink);letter-spacing:1px}
.contact-bar{right:96px;top:29px;display:flex;align-items:center;gap:14px;font-size:17px;color:var(--ink)}
.contact-bar span{display:flex;align-items:center;gap:9px}
.contact-bar .sep{color:var(--ink)}
.main-nav{right:96px;top:79px;display:flex;align-items:center;gap:34px;font-size:16px;letter-spacing:.4px}
.main-nav a{color:var(--ink);text-decoration:none}
.main-nav a.current{color:var(--rose)}

/* hero */
.hero-photo{left:0;top:134px;width:600px;height:521px;background:radial-gradient(ellipse at 45% 50%,#3a3a3a 0 22%,#cfcfcf 23%,#e6e6e6 60%,#dcdcdc 100%)}
.hero-panel{left:600px;top:134px;width:600px;height:521px;background:var(--blush)}
.hero-title{left:664px;top:232px;font-family:var(--script);font-size:82px;line-height:1;color:var(--ink)}
.hero-text{left:664px;top:356px;width:450px;font-family:var(--sans);font-size:17.5px;line-height:30px;color:var(--text)}
.btn{display:flex;align-items:center;justify-content:center;background:var(--ink);color:var(--white);font-family:var(--body);font-weight:700;font-size:15px;letter-spacing:.3px}
.hero-btn{left:664px;top:492px;width:166px;height:58px}

/* about */
.section-script{font-family:var(--script);font-size:66px;line-height:1;color:var(--ink)}
.about-title{left:0;width:1200px;top:752px;text-align:center}
.portrait{left:102px;top:848px;width:300px;height:300px;border-radius:50%;border:6px solid var(--white);box-shadow:0 0 0 1px #e3e3e3,0 2px 8px rgba(0,0,0,.18);background:radial-gradient(circle at 50% 45%,#e9d3b3 0 30%,#f2f2f2 31%,#f2f2f2 62%,#222 63%)}
.about-rule{left:462px;top:884px;width:1px;height:232px;background:var(--muted)}
.about-heading{left:529px;top:902px;font-family:var(--sans);font-weight:600;font-size:27px;color:var(--ink)}
.about-text{left:532px;top:960px;width:573px;font-family:var(--body);font-size:16px;line-height:28.6px;color:var(--text)}

/* services */
.services{left:0;top:1240px;width:1200px;height:594px;background:linear-gradient(100deg,#fbfaf8 0%,#f7f3ee 40%,#e9ddd0 62%,#d9c6b2 75%,#eeeae6 100%)}
.services-title{left:98px;top:1300px}
.services-text{left:98px;top:1390px;width:540px;font-family:var(--body);font-size:16px;line-height:28px;color:var(--text)}
.service-list{list-style:none;font-family:var(--sans);font-size:17px;color:var(--ink)}
.service-list li{display:flex;align-items:center;gap:12px;height:39px}
.list-a{left:98px;top:1467px}
.list-b{left:313px;top:1467px}
.services-btn{left:98px;top:1693px;width:150px;height:57px}

/* subscription */
.sub-title{left:0;width:1200px;top:1908px;text-align:center;font-weight:600;font-size:27px;color:var(--ink)}
.field{top:1971px;height:44px;border:1px solid var(--line);background:var(--white);font-family:var(--body);font-size:14px;color:#8a8a8a;padding-left:22px;display:flex;align-items:center}
.field-name{left:196px;width:324px}
.field-email{left:536px;width:322px}
.sub-btn{left:873px;top:1971px;width:131px;height:44px}

/* footer */
.social{left:484px;top:2061px;display:flex;gap:8px}
.social span{width:50px;height:50px;border:1px solid var(--rose);border-radius:50%;display:block}
.footer-nav{left:0;width:1200px;top:2137px;display:flex;justify-content:center;gap:24px;font-family:var(--body);font-size:14.5px;color:var(--text)}
.copyright{left:0;width:1200px;top:2183px;text-align:center;font-family:var(--body);font-size:14.5px;color:var(--text)}
</style>
</head>
<body>

<header>
  <div class="abs brand">Wren Pasco</div>
  <div class="abs contact-bar">
    <span><svg width="14" height="14" viewBox="0 0 24 24"><path fill="#d3868a" d="M6.6 10.8a15 15 0 0 0 6.6 6.6l2.2-2.2c.3-.3.7-.4 1-.2 1.1.4 2.3.6 3.6.6.6 0 1 .4 1 1V20c0 .6-.4 1-1 1A17 17 0 0 1 3 4c0-.6.4-1 1-1h3.5c.6 0 1 .4 1 1 0 1.3.2 2.5.6 3.6.1.3 0 .7-.2 1z"/></svg>(0438 526 914)</span>
    <span class="sep">|</span>
    <span><svg width="16" height="12" viewBox="0 0 16 12"><rect width="16" height="12" rx="1.5" fill="#d3868a"/><path d="M1 1.5l7 5 7-5" stroke="#fff" stroke-width="1.4" fill="none"/></svg>wren.pasco.copywriter@mailbrook.example</span>
  </div>
  <nav class="abs main-nav">
    <a class="current" href="#">HOME</a>
    <a href="#">SERVICES</a>
    <a href="#">PORTFOLIO</a>
    <a href="#">BLOG</a>
    <a href="#">CONTACT</a>
    <svg width="16" height="16" viewBox="0 0 16 16"><circle cx="6.5" cy="6.5" r="4.8" stroke="#1c1c1c" stroke-width="2.2" fill="none"/><path d="M10 10l4.5 4.5" stroke="#1c1c1c" stroke-width="2.6" stroke-linecap="round"/></svg>
  </nav>
</header>

<section>
  <div class="abs hero-photo" role="img" aria-label="Photo of a vintage black typewriter with a sheet of paper, seen from above on a light grey surface"></div>
  <div class="abs hero-panel"></div>
  <h1 class="abs hero-title" style="font-weight:400">wren pasco</h1>
  <p class="abs hero-text">Ut enim ad minima veniam, quis nostrum exercittionemu llam corporis suscipit laboriosam, nisi ut aliquid ex eacm modi consequatur vel eum iure reprehen.</p>
  <a class="abs btn hero-btn">GET MORE INFO</a>
</section>

<section>
  <h2 class="abs section-script about-title" style="font-weight:400">About Me</h2>
  <div class="abs portrait" role="img" aria-label="Portrait photo of the copywriter"></div>
  <div class="abs about-rule"></div>
  <h3 class="abs about-heading">I'M A FREELANCE COPYWRITER</h3>
  <p class="abs about-text">Nemo enim ipsam voluptatem quia voluptas sit aspernatur aut odit aut fugit, sed quia consequuntur magni dolores eos qui ratione voluptatem sequi nesciuntrtue porro quisquam est, qui dolorem ipsum quia dolor sit amet, consectetur, adipisci velit, sed quia non numquam eius modi tempora incidunt ut labore&nbsp; qui in ea volu ptate velit esse quam nihil molestiae consequatur.</p>
</section>

<section>
  <div class="abs services" role="img" aria-label="Soft-focus photo of hands typing on a laptop keyboard"></div>
  <h2 class="abs section-script services-title" style="font-weight:400">Services</h2>
  <p class="abs services-text">Eos qui ratione voluptatem sequi nesciuntrtue porro quisquam est, qui dolo rem ipsum quia dolor sit amet, consectetur, adipisci velit.</p>
  <ul class="abs service-list list-a">
    <li><svg width="15" height="15" viewBox="0 0 16 16"><circle cx="8" cy="8" r="8" fill="#d3868a"/><path d="M4.5 8.2l2.4 2.3 4.6-4.8" stroke="#fff" stroke-width="1.8" fill="none"/></svg>Website Copywriter</li>
    <li><svg width="15" height="15" viewBox="0 0 16 16"><circle cx="8" cy="8" r="8" fill="#d3868a"/><path d="M4.5 8.2l2.4 2.3 4.6-4.8" stroke="#fff" stroke-width="1.8" fill="none"/></svg>SEO Copywriter</li>
    <li><svg width="15" height="15" viewBox="0 0 16 16"><circle cx="8" cy="8" r="8" fill="#d3868a"/><path d="M4.5 8.2l2.4 2.3 4.6-4.8" stroke="#fff" stroke-width="1.8" fill="none"/></svg>Newsletters</li>
    <li><svg width="15" height="15" viewBox="0 0 16 16"><circle cx="8" cy="8" r="8" fill="#d3868a"/><path d="M4.5 8.2l2.4 2.3 4.6-4.8" stroke="#fff" stroke-width="1.8" fill="none"/></svg>Press Releases</li>
    <li><svg width="15" height="15" viewBox="0 0 16 16"><circle cx="8" cy="8" r="8" fill="#d3868a"/><path d="M4.5 8.2l2.4 2.3 4.6-4.8" stroke="#fff" stroke-width="1.8" fill="none"/></svg>Case Studies</li>
  </ul>
  <ul class="abs service-list list-b">
    <li><svg width="15" height="15" viewBox="0 0 16 16"><circle cx="8" cy="8" r="8" fill="#d3868a"/><path d="M4.5 8.2l2.4 2.3 4.6-4.8" stroke="#fff" stroke-width="1.8" fill="none"/></svg>Articles</li>
    <li><svg width="15" height="15" viewBox="0 0 16 16"><circle cx="8" cy="8" r="8" fill="#d3868a"/><path d="M4.5 8.2l2.4 2.3 4.6-4.8" stroke="#fff" stroke-width="1.8" fill="none"/></svg>Leaflets &amp; Brochures</li>
    <li><svg width="15" height="15" viewBox="0 0 16 16"><circle cx="8" cy="8" r="8" fill="#d3868a"/><path d="M4.5 8.2l2.4 2.3 4.6-4.8" stroke="#fff" stroke-width="1.8" fill="none"/></svg>Product Descriptions</li>
    <li><svg width="15" height="15" viewBox="0 0 16 16"><circle cx="8" cy="8" r="8" fill="#d3868a"/><path d="M4.5 8.2l2.4 2.3 4.6-4.8" stroke="#fff" stroke-width="1.8" fill="none"/></svg>Blog Writer</li>
  </ul>
  <a class="abs btn services-btn">READ MORE</a>
</section>

<section>
  <h2 class="abs sub-title">SUBSCRIPTION</h2>
  <div class="abs field field-name">Full Name</div>
  <div class="abs field field-email">Email Address</div>
  <a class="abs btn sub-btn">SUBMIT</a>
</section>

<footer>
  <div class="abs social" aria-label="Social media links">
    <span></span><span></span><span></span><span></span>
  </div>
  <nav class="abs footer-nav">
    <span>Home</span><span>|</span><span>Services</span><span>|</span><span>Portfolio</span><span>|</span><span>Blog</span><span>|</span><span>Contact.</span>
  </nav>
  <p class="abs copyright">Wren Pasco © 2018 All rights reserved.</p>
</footer>

</body>
</html>
```